5 x 7 card advertising ash spreading

I need a new design for a double sided 5 x 7 horizontal post card to give to funeral homes so they can give them out to people who are interested in an ash spreading boat charter at sea for their loved one who has died. I want a simple, professional, classy, thoughtful design that I can include a summary of what we offer, what's included, our logo and and contact info. Even though we will include the "what" we offer, this piece needs to speak to the readers "why". I've included an AI excerpt about why people desire this as opposed to being buried.
What we offer: Attended service, Unattended service, Memorial service, Anniversary service. What's included: Certificate of Ash Spreading, Onboard refreshments, Personalized music. Our contact information: Tidewell Charters, www.tidewellcharters.example, 452 Marlowe St., Clearwater, FL 33755, (727) 555-0148

Target Market(s)

People visiting a funeral home planning their own or a relatives final wishes for ash spreading at sea

Industry/Entity Type

Private boat charters

Requirements
Must have
• Professional look, speaks to they "why", as well as includes the "what" we do.

```html
<!DOCTYPE html>
<html lang="en">
<head>
<meta charset="utf-8">
<title>Ash Spreading Boat Charter Postcard</title>
<link rel="stylesheet" href="https://fonts.googleapis.com/css2?family=Cormorant+Garamond:ital,wght@0,400;0,500;1,400;1,500;1,700&family=Forum&family=Montserrat:wght@500&display=swap">
<style>
  :root {
    --backdrop: #7a7a7a;
    --navy: #0b2a44;
    --navy-soft: #1d3b57;
    --frame-gold: #f2dc3a;
    --label-gold: #f0a92a;
    --ink-light: #ffffff;
    --sea-dusk-top: #cdc2ae;
    --sea-dusk-mid: #6d7683;
    --sea-dusk-low: #34465c;
    --deep-sea: #0d1f30;
    --deep-sea-teal: #1b4a66;
  }
  * { box-sizing: border-box; margin: 0; padding: 0; }
  html, body {
    width: 1200px; height: 457px; overflow: hidden;
    background: var(--backdrop);
  }
  .sheet { position: relative; width: 1200px; height: 457px; }

  .card { position: absolute; top: 28px; height: 401px; overflow: hidden; }
  .card--front { left: 25px; width: 561px; }
  .card--back  { left: 614px; width: 561px; }

  .front-photo {
    position: absolute; inset: 0;
    background:
      linear-gradient(200deg, transparent 55%, rgba(235,230,225,0.55) 78%, rgba(200,190,180,0.35) 100%),
      linear-gradient(180deg, var(--sea-dusk-top) 0%, #a8a39b 12%, var(--sea-dusk-mid) 32%, var(--sea-dusk-low) 65%, #2b3a4e 100%);
  }
  .frame {
    position: absolute; border: 1.5px solid var(--frame-gold);
  }
  .card--front .frame { left: 20px; top: 20px; width: 521px; height: 341px; }
  .card--back .frame  { left: 20px; top: 20px; width: 522px; height: 341px; }

  .contact-band {
    position: absolute; left: 335px; top: 0; width: 187px; height: 401px;
    background: linear-gradient(180deg, var(--navy) 0%, var(--navy-soft) 45%, #2a4560 62%, var(--navy) 100%);
    color: var(--ink-light);
    font-family: "Cormorant Garamond", serif;
    font-style: italic; font-weight: 500;
    text-align: center;
  }
  .brand-mark {
    position: absolute; left: 0; right: 0; top: 96px;
    font-family: "Cormorant Garamond", serif; font-style: normal; font-weight: 500;
    font-size: 23px; line-height: 1.05; letter-spacing: 0.5px;
  }
  .brand-mark .dot {
    display: block; width: 10px; height: 10px; margin: 0 auto 8px;
    border: 1.5px solid var(--frame-gold); border-radius: 50%;
  }
  .contact-address { position: absolute; left: 0; right: 0; top: 205px; font-size: 15.5px; line-height: 21px; }
  .contact-phone   { position: absolute; left: 0; right: 0; top: 270px; font-size: 15.5px; }
  .contact-web     { position: absolute; left: 0; right: 0; top: 313px; font-size: 13px; }

  .front-title {
    position: absolute; left: 0; width: 335px; top: 150px;
    text-align: center; color: var(--ink-light);
  }
  .front-title h1 {
    font-family: "Forum", serif; font-weight: 400;
    font-variant: small-caps; font-size: 64px; line-height: 45px; letter-spacing: -1px;
  }
  .front-title p {
    margin-top: 22px;
    font-family: "Montserrat", sans-serif; font-weight: 500;
    font-size: 15px; letter-spacing: 1px;
  }

  .back-photo {
    position: absolute; inset: 0;
    background:
      radial-gradient(ellipse 55% 45% at 18% 92%, rgba(170,200,215,0.55), transparent 70%),
      radial-gradient(ellipse 50% 60% at 30% 25%, rgba(40,90,120,0.55), transparent 70%),
      linear-gradient(120deg, var(--deep-sea-teal) 0%, #143650 40%, var(--deep-sea) 100%);
  }
  .why-statement {
    position: absolute; left: 47px; top: 67px; width: 275px;
    font-family: "Cormorant Garamond", serif; font-style: italic; font-weight: 500;
    font-size: 21px; line-height: 25.4px; color: var(--ink-light);
  }
  .why-statement strong { font-weight: 700; }

  .offer-list {
    position: absolute; left: 332px; width: 210px; text-align: center; color: var(--ink-light);
  }
  .offer-list--services { top: 102px; }
  .offer-list--included { top: 264px; }
  .offer-list h2 {
    font-family: "Montserrat", sans-serif; font-weight: 500;
    font-size: 9.5px; letter-spacing: 1.6px; color: var(--label-gold);
  }
  .offer-list .dot {
    display: block; width: 5px; height: 5px; margin: 5px auto 4px;
    border: 1px solid var(--ink-light); border-radius: 50%;
  }
  .offer-list li {
    list-style: none;
    font-family: "Cormorant Garamond", serif; font-style: italic; font-weight: 500;
    font-size: 15.5px; line-height: 22.4px;
  }
</style>
</head>
<body>
<main class="sheet">
  <section class="card card--front">
    <div class="front-photo" role="img" aria-label="Photo of calm sea at dusk seen from the bow of a sailboat"></div>
    <div class="frame"></div>
    <div class="front-title">
      <h1>Ash<br>Spreading</h1>
      <p>BOAT CHARTER</p>
    </div>
    <div class="contact-band">
      <div class="brand-mark"><span class="dot"></span>Tidewell<br>Charters</div>
      <p class="contact-address">452 Marlowe St.,<br>Clearwater, FL 33755</p>
      <p class="contact-phone">(727) 555-0148</p>
      <p class="contact-web">www.tidewellcharters.example</p>
    </div>
  </section>

  <section class="card card--back">
    <div class="back-photo" role="img" aria-label="Aerial photo of dark ocean water with white surf"></div>
    <div class="frame"></div>
    <p class="why-statement"><strong>Spreading ashes</strong> at sea symbolizes a deep connection to nature, representing a return to the elements and a sense of eternal continuity.</p>
    <div class="offer-list offer-list--services">
      <h2>WHAT WE OFFER</h2>
      <span class="dot"></span>
      <ul>
        <li>Attended Service</li>
        <li>Unattended Service</li>
        <li>Memorial Service</li>
        <li>Anniversary Service</li>
      </ul>
    </div>
    <div class="offer-list offer-list--included">
      <h2>WHAT’S INCLUDED</h2>
      <span class="dot"></span>
      <ul>
        <li>Certificate of Ash Spreading</li>
        <li>Onboard Refreshments</li>
        <li>Personalized Music</li>
      </ul>
    </div>
  </section>
</main>
</body>
</html>
```